Stationary for Hair Cosmetic company

We mainly sell hair thickening products www.morvello-wellform.de/morvello-hair/ Hair thickening products are a smart and easy solution for thinning hair for both men and women. We sell very information oriented in an honest undramatic manner.

We would like to see a decent color and style that is suitable for men and women. It shall be rather modern with a vintage spin as our own product (Morvello Bottle). Please use our logo (attatched).

Please bias your design to the bottle. To give you an idea: Chalk design like http://de.pixaverum.com/id/48213597 or one-color watercolor like http://de.pixaverum.com/id/63925180 is appreciated but not necessary.

Good but rejected designs will get compensation.

Target Market(s)

Wide range in demographics: age 20-55; 45% male, 55% women; issues with hair loss; self-conscious

Industry/Entity Type

Hair

Colors
3377b5
33a6d7
32b7a4
cbdf83
fbf289
fee18a
f9bb93
f05157

Requirements
Must have
• trustworthiness
Nice to have
• Chalk design like http://de.pixaverum.com/id/48213597 or one-color watercolor like http://de.pixaverum.com/id/63925180 is appreciated but not necessary

```html
<!DOCTYPE html>
<html lang="en">
<head>
<meta charset="utf-8">
<title>Morvello Letterhead</title>
<link href="https://fonts.googleapis.com/css2?family=Tinos:ital,wght@0,400;0,700;1,400&family=Didact+Gothic&display=swap" rel="stylesheet">
<style>
  :root {
    --backdrop: #e4e4e4;
    --paper: #ffffff;
    --ink: #1c1c1c;
    --ink-soft: #555555;
    --accent-grey: #b9b9b9;
    --accent-faint: #d6d6d6;
  }
  html, body {
    margin: 0;
    width: 1200px;
    height: 909px;
    overflow: hidden;
    background: var(--backdrop);
  }
  .letterhead {
    position: absolute;
    left: 264px;
    top: 20px;
    width: 672px;
    height: 869px;
    background: var(--paper);
    box-shadow: 0 2px 10px rgba(0,0,0,0.12);
    overflow: hidden;
    font-family: "Tinos", "Times New Roman", serif;
    color: var(--ink);
  }
  .brand {
    position: absolute;
    left: 62px;
    top: 48px;
    display: flex;
    align-items: center;
    gap: 10px;
  }
  .brand-dot {
    width: 14px;
    height: 14px;
    border-radius: 50%;
    background: var(--ink);
  }
  .brand-name {
    font-family: "Tinos", "Times New Roman", serif;
    font-size: 17px;
    letter-spacing: 3px;
    color: var(--ink);
  }
  .letter {
    position: absolute;
    left: 62px;
    top: 120px;
    width: 548px;
    font-size: 12.5px;
    line-height: 1.32;
    text-align: justify;
  }
  .letter p { margin: 0 0 14px; }
  .letter .salutation { margin-bottom: 12px; }
  .closing {
    position: absolute;
    left: 62px;
    top: 468px;
    font-size: 12.5px;
    line-height: 1.35;
    font-weight: 700;
  }
  .signature {
    display: block;
    margin: 6px 0 4px;
  }
  .corner-shape {
    position: absolute;
    right: -120px;
    bottom: -120px;
  }
  .contact {
    position: absolute;
    left: 62px;
    top: 718px;
    font-family: "Didact Gothic", "Helvetica", sans-serif;
    font-size: 10.5px;
    line-height: 1.55;
    color: var(--ink-soft);
  }
  .contact-line { display: flex; align-items: center; gap: 8px; }
  .contact-line svg { width: 11px; height: 11px; }
  .contact .address { margin-bottom: 4px; }
</style>
</head>
<body>
  <main class="letterhead">
    <header class="brand">
      <span class="brand-dot"></span>
      <span class="brand-name">MORVELLO</span>
    </header>

    <article class="letter">
      <p class="salutation">Gentlemen,</p>
      <p>Enclosed I have the honor to send you an article which I should be pleased if you would accept for the “Meridian Quarterly.” I am <em>desperately</em> pushed for money; and in the event of Mr. Hallorant’s liking the “Landscape-Garden”, I would take it as an especial favor if you would mail me the amount due for it, so as to reach me here by the 21st, on which day I shall need it. Can you possibly oblige me in this? If you accept the paper I presume you will allow me your usual sum, whatever that is for similar contributions—but I set no price—leaving all to your own liberality. The piece will make 8 of your pages and rather more.</p>
      <p>Will you be kind enough to put the best possible interpretation upon my behavior while in Ashbury? You must have conceived a <em>queer</em> idea of me—but the simple truth is that Tremaine would insist upon <em>the juleps</em>, and I knew not what I was either doing or saying. The Review of Corwen which I offered you was deficient in a 1/2 page at the commencement, which I had written to supersede the old beginning, and which gave the article the character of a general and retrospective review. No wonder you did not take it—I would have been very much mortified if you had. I hope to see you at some future time, under better auspices.</p>
    </article>

    <section class="closing">
      <div>In the meantime I remain</div>
      <div>Yours very truly,</div>
      <svg class="signature" width="90" height="30" viewBox="0 0 90 30" role="img" aria-label="Handwritten signature of Elias Ambrose Penwick">
        <rect x="0" y="6" width="86" height="20" rx="3" fill="var(--accent-faint)"/>
      </svg>
      <div>Elias Ambrose Penwick</div>
    </section>

    <svg class="corner-shape" width="330" height="330" viewBox="0 0 330 330" aria-hidden="true">
      <circle cx="165" cy="165" r="160" fill="var(--accent-faint)"/>
    </svg>

    <footer class="contact">
      <div class="address">2281 Larkmoor Ridge<br>Fallbrook, CA 92028</div>
      <div class="contact-line">
        <svg viewBox="0 0 12 12" aria-hidden="true"><path d="M1 4 Q6 0 11 4 L9 5.5 L8 4 L4 4 L3 5.5 Z M3 6 L9 6 L10 11 L2 11 Z" fill="var(--ink-soft)"/></svg>
        <span>760-555-0142</span>
      </div>
      <div class="contact-line">
        <svg viewBox="0 0 12 12" aria-hidden="true"><rect x="3" y="0.5" width="6" height="11" rx="1" fill="none" stroke="var(--ink-soft)"/><circle cx="6" cy="9.5" r="0.8" fill="var(--ink-soft)"/></svg>
        <span>760-555-0187</span>
      </div>
      <div class="contact-line">
        <svg viewBox="0 0 12 12" aria-hidden="true"><rect x="0.5" y="2.5" width="11" height="7" fill="none" stroke="var(--ink-soft)"/><path d="M0.5 2.5 L6 7 L11.5 2.5" fill="none" stroke="var(--ink-soft)"/></svg>
        <span>nora@morvello.com</span>
      </div>
    </footer>
  </main>
</body>
</html>
```